DRIFTFRAME studio

Design to be modern with colours of logo, maybe orange background. Include name, position, phone/WhatsApp email/web. Specialises in long form TIMELAPSE

Contact Information for Business Card

Marcel Okoro, filmmaker,/photographer, phone/WhatsApp +971529386047, email - marcel@driftframestudio.com www.driftframestudio.com, instagram @driftframestudio

Font styles to use
Sans Serif

Requirements
Must have
• Fresh, bright, modern, original
Marcel Okoro - Filmmaker/Photographer
Phone/WhatsApp +971 529 38 6047
email - marcel@driftfarmestudio.com
Web - driftfarmestudio.com
PoBox 584319, Dubai, UAE
instagram - driftframestudio
Should not have
• solid black background

```html
<!DOCTYPE html>
<html lang="en">
<head>
<meta charset="utf-8">
<title>DRIFTFRAME studio – Business Card</title>
<link rel="stylesheet" href="https://fonts.googleapis.com/css2?family=Lato:wght@400;700;900&display=swap">
<style>
  :root {
    --backdrop: #f37722;
    --brand-orange: #ff7300;
    --card-white: #ffffff;
    --ink-black: #000000;
    --text-white: #ffffff;
  }
  * { margin: 0; padding: 0; box-sizing: border-box; }
  html, body {
    width: 1200px; height: 1058px; overflow: hidden;
    background: var(--backdrop);
    font-family: "Lato", sans-serif;
  }
  .canvas { position: relative; width: 1200px; height: 1058px; }

  .card {
    position: absolute; left: 316px; width: 635px; height: 381px;
    background: var(--card-white); overflow: hidden;
  }
  .card--front { top: 103px; }
  .card--back { top: 571px; }

  /* Front */
  .front-band {
    position: absolute; left: 0; top: 293px; width: 100%; height: 88px;
    background: var(--ink-black);
  }
  .front-wordmark {
    position: absolute; left: 0; top: 90px; width: 100%;
    text-align: center;
  }
  .web-pill {
    position: absolute; left: 201px; top: 272px; width: 234px; height: 44px;
    background: var(--brand-orange); border-radius: 22px 22px 22px 22px;
    color: var(--text-white); font-size: 15.5px; font-weight: 400;
    display: flex; align-items: center; justify-content: center;
  }

  /* Wordmark (invented name, one colour, one weight) */
  .wordmark {
    display: inline-flex; align-items: center; gap: 12px;
    color: var(--brand-orange); font-weight: 900; letter-spacing: 0.5px;
    line-height: 1;
  }
  .wordmark__dot {
    width: 22px; height: 22px; border-radius: 50%;
    background: var(--brand-orange); flex: none;
  }
  .front-wordmark .wordmark { font-size: 40px; }
  .back-wordmark {
    position: absolute; left: 0; top: 164px; width: 296px; text-align: center;
  }
  .back-wordmark .wordmark { font-size: 25px; gap: 8px; }
  .back-wordmark .wordmark__dot { width: 16px; height: 16px; }

  /* Back */
  .back-shapes { position: absolute; left: 0; top: 0; }
  .person-name {
    position: absolute; left: 359px; top: 87px;
    color: var(--brand-orange); font-weight: 700; font-size: 24px;
    letter-spacing: -0.2px; white-space: nowrap;
  }
  .person-role {
    position: absolute; left: 366px; top: 113px;
    color: var(--text-white); font-weight: 700; font-size: 15.5px;
    white-space: nowrap;
  }
  .contact-line {
    position: absolute; left: 359px;
    color: var(--text-white); font-size: 14px; font-weight: 400;
    white-space: nowrap;
  }
  .contact-line--phone { top: 189px; }
  .contact-line--email { top: 238px; }
  .contact-line--web { top: 287px; }
  .contact-line--social { top: 334px; }
</style>
</head>
<body>
<div class="canvas">

  <section class="card card--front">
    <div class="front-wordmark">
      <span class="wordmark"><span class="wordmark__dot"></span>DRIFTFRAME studio</span>
    </div>
    <div class="front-band"></div>
    <div class="web-pill">www.driftframestudio.com</div>
  </section>

  <section class="card card--back">
    <div class="back-wordmark">
      <span class="wordmark"><span class="wordmark__dot"></span>DRIFTFRAME studio</span>
    </div>

    <svg class="back-shapes" width="635" height="381" viewBox="0 0 635 381" aria-hidden="true">
      <rect x="296" y="0" width="43" height="381" fill="var(--brand-orange)"/>
      <rect x="339" y="0" width="296" height="381" fill="var(--ink-black)"/>
      <!-- black tab reaching into the orange strip -->
      <path d="M339 118 L339 180 L317 180 Q317 168 330 162 Q317 156 317 148 L317 150 Q317 126 339 118 Z" fill="var(--ink-black)"/>
      <rect x="317" y="127" width="22" height="43" fill="var(--ink-black)"/>
      <path d="M317 127 Q317 118 339 110 L339 127 Z" fill="var(--brand-orange)"/>
      <path d="M317 170 Q317 180 339 188 L339 170 Z" fill="var(--brand-orange)"/>

      <!-- icon discs -->
      <g fill="var(--ink-black)">
        <circle cx="317.5" cy="102.7" r="16.5"/>
        <circle cx="317.5" cy="196.6" r="16.5"/>
        <circle cx="317.5" cy="245.3" r="16.5"/>
        <circle cx="317.5" cy="294.7" r="16.5"/>
        <circle cx="317.5" cy="342.2" r="16.5"/>
      </g>
      <g fill="none" stroke="var(--text-white)" stroke-width="1.2">
        <circle cx="317.5" cy="196.6" r="13.5"/>
        <circle cx="317.5" cy="245.3" r="13.5"/>
        <circle cx="317.5" cy="294.7" r="13.5"/>
        <circle cx="317.5" cy="342.2" r="13.5"/>
      </g>

      <!-- person icon -->
      <g fill="var(--text-white)">
        <circle cx="317.5" cy="99" r="4"/>
        <path d="M310 110 Q310 103.5 317.5 103.5 Q325 103.5 325 110 Z"/>
      </g>
      <!-- phone icon -->
      <path d="M312 190 Q310 192 311.5 195.5 Q314 201 319.5 203 Q322.5 204 324 202 L324.5 200.5 L321.5 198.5 L319.8 200 Q316 198 314.5 194.5 L316 193 L314 190 Z" fill="var(--text-white)"/>
      <!-- house icon -->
      <path d="M317.5 237.5 L309 245 L311 245 L311 252 L315.5 252 L315.5 248 L319.5 248 L319.5 252 L324 252 L324 245 L326 245 Z" fill="var(--text-white)"/>
      <!-- globe icon -->
      <g fill="none" stroke="var(--text-white)" stroke-width="1.3">
        <circle cx="317.5" cy="294.7" r="7.5"/>
        <ellipse cx="317.5" cy="294.7" rx="3.2" ry="7.5"/>
        <line x1="310" y1="294.7" x2="325" y2="294.7"/>
      </g>
      <!-- social handle marker -->
      <circle cx="317.5" cy="342.2" r="4" fill="var(--text-white)"/>
    </svg>

    <p class="person-name">MARCEL OKORO</p>
    <p class="person-role">filmmaker,/photographer</p>
    <p class="contact-line contact-line--phone">+971529386047</p>
    <p class="contact-line contact-line--email">marcel@driftframestudio.com</p>
    <p class="contact-line contact-line--web">www.driftframestudio.com</p>
    <p class="contact-line contact-line--social">@driftframestudio</p>
  </section>

</div>
</body>
</html>
```